Single-page, simple & clean, departure board web app

TrellisHop.com provides easy to use train schedule information in Chicago, IL between downtown and Hyde Park. The site has been around for about 3 years and the design has not changed since the weekend hackathon at which it was created. Now, it has a solid user base and is in dire need of a fresh design.
The design should be super-clean and intuitive. It is used by the type of people who love the style and personality of sites like Gravlox. The design should incorporate the maroon color that is used extensively on the existing site. The main features are (1) the train depart times, (2) the fact that different stations can be selected as departure/arrival, (3) the fact that a user can click "earlier trains" or "later trains" to quickly scan the times.
This is a single-page web app that displays static content. The design should reflect that 100% of the users time is spent on the single page. There is no "sign up" process or external aspect. All focus should be used to design the best possible display of train times.
Target Market(s)
24-30 yr old, middle to upper income, opinionated, heavily international
Look and feel
Each slider illustrates characteristics of the customer's brand and the style your logo design should communicate.

```html
<!DOCTYPE html>
<html lang="en">
<head>
<meta charset="utf-8">
<title>TrellisHop – Train Times</title>
<link rel="stylesheet" href="https://fonts.googleapis.com/css2?family=Ubuntu:wght@400;500;700&family=Arimo:ital,wght@0,400;0,700;1,400&display=swap">
<style>
  :root {
    --maroon: #7d1f30;
    --maroon-dark: #5e1220;
    --maroon-band: #8a2236;
    --maroon-text: #8c1c30;
    --header-bg: #f3f3f3;
    --ink: #2b2b2b;
    --tab-off: #d6d6d6;
    --tab-text: #8a8a8a;
    --footer-text: #e6c9cf;
  }
  * { box-sizing: border-box; margin: 0; padding: 0; }
  html, body { width: 1200px; height: 800px; overflow: hidden; }
  body {
    position: relative;
    font-family: "Arimo", Arial, sans-serif;
    color: var(--ink);
    background-color: var(--maroon);
    background-image:
      repeating-linear-gradient(0deg, rgba(255,255,255,.035) 0 1px, transparent 1px 16px),
      repeating-linear-gradient(90deg, rgba(255,255,255,.035) 0 1px, transparent 1px 16px);
  }
  .site-header {
    position: absolute; left: 0; top: 0; width: 1200px; height: 79px;
    background-color: var(--header-bg);
    background-image:
      repeating-linear-gradient(0deg, rgba(0,0,0,.04) 0 1px, transparent 1px 12px),
      repeating-linear-gradient(90deg, rgba(0,0,0,.04) 0 1px, transparent 1px 12px);
  }
  .brand-name {
    position: absolute; left: 352px; top: 18px;
    font-family: "Ubuntu", sans-serif; font-weight: 700; font-size: 34px;
    color: var(--maroon-text); letter-spacing: -.5px;
  }
  .tagline {
    position: absolute; right: 222px; top: 28px; text-align: right;
    font-family: "Ubuntu", sans-serif; font-size: 10.5px; line-height: 14.5px; color: #333;
  }
  .mascot {
    position: absolute; border-radius: 40%;
    background: radial-gradient(circle at 50% 40%, #b87a45, #6b6470 70%, transparent 72%);
  }
  .mascot-top { left: 216px; top: 0; width: 124px; height: 124px; }
  .mascot-bottom { left: 884px; top: 672px; width: 130px; height: 128px; }
  .nav-band {
    position: absolute; left: 0; width: 1200px; height: 48px;
    background: linear-gradient(180deg, var(--maroon-band), var(--maroon));
    border-top: 1px solid #a13146; border-bottom: 1px solid #9c2a40;
  }
  .nav-band.to-campus { top: 79px; }
  .nav-band.to-downtown { top: 388px; }
  .nav-btn {
    position: absolute; top: 4px; height: 40px; width: 114px;
    border-radius: 20px; background: var(--maroon-dark);
    box-shadow: inset 0 1px 3px rgba(0,0,0,.5);
    font-size: 13px; font-weight: 700; color: #f0dfe2;
    display: flex; align-items: center; justify-content: center; gap: 4px;
  }
  .nav-btn.earlier { left: 366px; }
  .nav-btn.later { left: 703px; }
  .nav-btn svg { width: 10px; height: 14px; }
  .direction-title {
    position: absolute; left: 480px; width: 230px; top: 0; line-height: 46px; text-align: center;
    font-family: "Ubuntu", sans-serif; font-weight: 500; font-size: 19px; color: #fff;
  }
  .station-tabs { position: absolute; display: flex; align-items: flex-end; }
  .station-tabs.campus { left: 238px; top: 128px; }
  .station-tabs.downtown { left: 228px; top: 438px; }
  .tab {
    height: 24px; padding-top: 5px; text-align: center;
    font-size: 11px; font-weight: 700; color: var(--tab-text);
    background: linear-gradient(180deg, #ececec, var(--tab-off));
    border-radius: 6px 6px 0 0; margin-right: 1px;
  }
  .tab.active { background: #f8f8f8; color: var(--maroon-text); }
  .schedule-panel {
    position: absolute; left: 216px; width: 769px;
    background: linear-gradient(180deg, #fdfdfd, #e2e2e2);
    border-radius: 8px;
  }
  .schedule-panel.campus { top: 152px; height: 236px; }
  .schedule-panel.downtown { top: 462px; height: 275px; }
  .train { position: absolute; left: 9px; right: 9px; }
  .train + .train { border-top: 1px solid #9a9a9a; }
  .train-name {
    position: absolute; left: 22px; top: 0;
    font-size: 14px; font-weight: 700; color: var(--maroon-text);
  }
  .train-name small { display: block; font-size: 9.5px; font-weight: 400; font-style: italic; color: #444; margin-top: 2px; }
  .stops { position: absolute; top: 2px; font-size: 11px; font-weight: 700; line-height: 19.2px; white-space: nowrap; }
  .stops div { display: flex; }
  .stops dt { width: 58px; }
  .footer {
    position: absolute; left: 0; width: 1134px; text-align: center; color: var(--footer-text);
  }
  .footer.updated { top: 749px; font-size: 11.5px; }
  .footer.footer-links { top: 773px; font-size: 9.5px; }
</style>
</head>
<body>
  <header class="site-header">
    <div class="brand-name">TrellisHop</div>
    <p class="tagline">Lakefront Electric between Downtown Chicago and Hydeview School<br>Designed for home, school, and mobile access</p>
  </header>
  <div class="mascot mascot-top" role="img" aria-label="Cartoon mascot illustration holding a flag and a banana"></div>

  <nav class="nav-band to-campus">
    <a class="nav-btn earlier"><svg viewBox="0 0 10 14"><path d="M8 1 2 7l6 6" fill="none" stroke="#f0dfe2" stroke-width="2.4"/></svg>earlier trains</a>
    <h2 class="direction-title">To Hydeview School</h2>
    <a class="nav-btn later">later trains<svg viewBox="0 0 10 14"><path d="M2 1l6 6-6 6" fill="none" stroke="#f0dfe2" stroke-width="2.4"/></svg></a>
  </nav>
  <div class="station-tabs campus">
    <span class="tab active" style="width:100px">from millenium</span>
    <span class="tab" style="width:96px">from van buren</span>
    <span class="tab" style="width:95px">from 11th</span>
  </div>
  <section class="schedule-panel campus">
    <article class="train" style="top:12px;height:82px">
      <h3 class="train-name">Train # 305</h3>
      <dl class="stops" style="left:269px"><div><dt>Depart:</dt><dd>6:28 am from Millennium Station</dd></div><div><dt>Arrive:</dt><dd>6:42 am at 51st-53rd Street</dd></div><div><dt>Arrive:</dt><dd>6:44 am at 55th-56th-57th Street</dd></div><div><dt>Arrive:</dt><dd>6:46 am at 59th Street</dd></div></dl>
    </article>
    <article class="train" style="top:94px;height:52px">
      <h3 class="train-name" style="top:10px">Train # 105<small>Express</small></h3>
      <dl class="stops" style="left:268px;top:8px"><div><dt>Depart:</dt><dd>6:35 am from Millennium Station</dd></div><div><dt>Arrive:</dt><dd>6:47 am at 55th-56th-57th Street</dd></div></dl>
    </article>
    <article class="train" style="top:146px;height:88px">
      <h3 class="train-name" style="top:9px">Train # 307</h3>
      <dl class="stops" style="left:267px;top:3px"><div><dt>Depart:</dt><dd>6:50 am from Millennium Station</dd></div><div><dt>Arrive:</dt><dd>7:04 am at 51st-53rd Street</dd></div><div><dt>Arrive:</dt><dd>7:06 am at 55th-56th-57th Street</dd></div><div><dt>Arrive:</dt><dd>7:08 am at 59th Street</dd></div></dl>
    </article>
  </section>

  <nav class="nav-band to-downtown">
    <a class="nav-btn earlier"><svg viewBox="0 0 10 14"><path d="M8 1 2 7l6 6" fill="none" stroke="#f0dfe2" stroke-width="2.4"/></svg>earlier trains</a>
    <h2 class="direction-title">To Downtown</h2>
    <a class="nav-btn later">later trains<svg viewBox="0 0 10 14"><path d="M2 1l6 6-6 6" fill="none" stroke="#f0dfe2" stroke-width="2.4"/></svg></a>
  </nav>
  <div class="station-tabs downtown">
    <span class="tab active" style="width:99px">from 51st-53rd</span>
    <span class="tab" style="width:95px">from 55th-57th</span>
    <span class="tab" style="width:95px">from 59th</span>
    <span class="tab" style="width:106px">from 57th or 59th</span>
  </div>
  <section class="schedule-panel downtown">
    <article class="train" style="top:14px;height:77px">
      <h3 class="train-name">Train # 102</h3>
      <dl class="stops" style="left:263px;top:-1px"><div><dt>Depart:</dt><dd>6:09 am from 59th Street</dd></div><div><dt>Arrive:</dt><dd>6:24 am at 11th Street</dd></div><div><dt>Arrive:</dt><dd>6:27 am at Van Buren Street</dd></div><div><dt>Arrive:</dt><dd>6:30 am at Millennium Station</dd></div></dl>
    </article>
    <article class="train" style="top:91px;height:89px">
      <h3 class="train-name" style="top:9px">Train # 204</h3>
      <dl class="stops" style="left:261px;top:7px"><div><dt>Depart:</dt><dd>6:47 am from 59th Street</dd></div><div><dt>Arrive:</dt><dd>7:00 am at 11th Street</dd></div><div><dt>Arrive:</dt><dd>7:03 am at Van Buren Street</dd></div><div><dt>Arrive:</dt><dd>7:06 am at Millennium Station</dd></div></dl>
    </article>
    <article class="train" style="top:180px;height:92px">
      <h3 class="train-name" style="top:7px">Train # 304</h3>
      <dl class="stops" style="left:259px;top:5px"><div><dt>Depart:</dt><dd>6:50 am from 59th Street</dd></div><div><dt>Arrive:</dt><dd>7:05 am at 11th Street</dd></div><div><dt>Arrive:</dt><dd>7:08 am at Van Buren Street</dd></div><div><dt>Arrive:</dt><dd>7:11 am at Millennium Station</dd></div></dl>
    </article>
  </section>
  <div class="mascot mascot-bottom" role="img" aria-label="Cartoon mascot illustration waving a flag"></div>

  <p class="footer updated">Train Schedule Last Updated: January 15, 2012</p>
  <p class="footer footer-links">Terms and conditions of use | Questions or comments</p>
</body>
</html>
```